Consulting and Personal Growth company needs instagram design

Design of Instagram feed.
Please see attached:
1. Design brief with all details and mood board
2. Posts texts
3. Brand logo and colors

Objective:
Design Instagram feed for The Lumen Compass so that the posts flow visually while each post looks beautiful by itself. The posts have the following order:

THEME: 1 PURPOSE - 3 posts
HEALTH - 3 posts
MIND - 3 posts
VISION - 3 posts
Every post will be posted independently (not in groups of 3)
Use @thelumencompass in all posts. (See post texts in attachment)

Target Market(s)

Business owners and executives, men and women who want to maximize their potential and impact.

Industry/Entity Type

Consulting

Font styles to use
Other font styles liked:
• Avenir

Requirements
Must have
• Clean, professional design
• Beautiful flow of posts in feed
• Eye-catching independent posts
• Feed is not disrupted when adding a new post
• Use @thelumencompass in all posts.
Nice to have
• Logo "star" can be used in posts if it helps build branding but not mandatory.
Should not have
• Each post independent with no flow/beautiful design of feed.

```html
<!DOCTYPE html>
<html lang="en">
<head>
<meta charset="utf-8">
<title>The Lumen Compass — Instagram Feed</title>
<link href="https://fonts.googleapis.com/css2?family=Nunito+Sans:ital,wght@0,300;0,400;1,300&display=swap" rel="stylesheet">
<style>
  :root {
    --ink: #1c1c1c;
    --white: #ffffff;
    --vision: #bcbc22;
    --vision-word: #b7b71f;
    --mind: #b9121a;
    --mind-word: #c2161d;
    --health: #1dbb15;
    --health-word: #2db81d;
    --purpose: #2a39bd;
    --purpose-word: #2b3ab8;
  }
  * { margin: 0; padding: 0; box-sizing: border-box; }
  html, body {
    width: 900px; height: 1200px; overflow: hidden; background: var(--white);
  }
  .feed {
    width: 900px; height: 1200px;
    display: grid;
    grid-template-columns: repeat(3, 300px);
    grid-template-rows: repeat(4, 300px);
    font-family: "Nunito Sans", "Avenir", sans-serif;
    color: var(--ink);
  }
  .post { position: relative; overflow: hidden; }
  .post--vision  { background: linear-gradient(to bottom, var(--white) 0%, var(--white) 42%, var(--vision) 100%); }
  .post--mind    { background: linear-gradient(to bottom, var(--white) 0%, var(--white) 42%, var(--mind) 100%); }
  .post--health  { background: linear-gradient(to bottom, var(--white) 0%, var(--white) 45%, var(--health) 100%); }
  .post--purpose { background: linear-gradient(to bottom, var(--white) 0%, var(--white) 52%, var(--purpose) 100%); }

  .quote {
    position: absolute; left: 0; top: 0;
    width: 300px; height: 178px;
    display: flex; flex-direction: column; justify-content: flex-end;
    align-items: center; text-align: center;
  }
  .quote__text {
    font-weight: 300; font-size: 17.4px; line-height: 21.6px;
    white-space: nowrap; letter-spacing: 0.1px;
  }
  .quote__author {
    font-weight: 300; font-style: italic; font-size: 14.4px;
    line-height: 22px; margin-top: 1px;
  }
  .post--health .quote--plain { height: 174px; }
  .keyword { font-weight: 300; }
  .post--vision  .keyword { color: var(--vision-word); }
  .post--mind    .keyword { color: var(--mind-word); }
  .post--health  .keyword { color: var(--health-word); }
  .post--purpose .keyword { color: var(--purpose-word); }

  .handle {
    position: absolute; left: 6px; bottom: 5px;
    color: var(--white); font-weight: 300; font-size: 15.4px;
  }
</style>
</head>
<body>
<main class="feed">

  <section class="post post--vision">
    <div class="quote">
      <p class="quote__text">If you don’t have a <span class="keyword">VISION</span><br>of your ideal life you will<br>never live that life.<br>Get clear on your vision.</p>
      <p class="quote__author">- Mara Vellini</p>
    </div>
    <span class="handle">@thelumencompass</span>
  </section>

  <section class="post post--vision">
    <div class="quote">
      <p class="quote__text">When you have a clear <span class="keyword">VISION</span><br>of how to navigate your life,<br>you maximize your happiness<br>and sense of fulfillment.</p>
      <p class="quote__author">- Mara Vellini</p>
    </div>
    <span class="handle">@thelumencompass</span>
  </section>

  <section class="post post--vision">
    <div class="quote">
      <p class="quote__text">Everyone, including you can<br>design a <span class="keyword">VISION</span><br>of an extraordinary life you love.</p>
      <p class="quote__author">- Mara Vellini</p>
    </div>
    <span class="handle">@thelumencompass</span>
  </section>

  <section class="post post--mind">
    <div class="quote">
      <p class="quote__text">Your <span class="keyword">MIND</span> needs you<br>to be clear on what you want<br>so that it can help you achieve it.<br>Get clear.</p>
      <p class="quote__author">- Mara Vellini</p>
    </div>
    <span class="handle">@thelumencompass</span>
  </section>

  <section class="post post--mind">
    <div class="quote">
      <p class="quote__text">When you understand and master<br>how your <span class="keyword">MIND</span> works you<br>expand your life’s<br>potential and possibilities.</p>
      <p class="quote__author">- Mara Vellini</p>
    </div>
    <span class="handle">@thelumencompass</span>
  </section>

  <section class="post post--mind">
    <div class="quote">
      <p class="quote__text">Maximize your <span class="keyword">MIND</span> to enhance<br>your focus, tap your intuition<br>and maximize your creativity.</p>
      <p class="quote__author">- Mara Vellini</p>
    </div>
    <span class="handle">@thelumencompass</span>
  </section>

  <section class="post post--health">
    <div class="quote quote--plain">
      <p class="quote__text">Your <span class="keyword">HEALTH</span> is the foundation<br>for living an extraordinary life.<br>How healthy are you right now?</p>
    </div>
    <span class="handle">@thelumencompass</span>
  </section>

  <section class="post post--health">
    <div class="quote">
      <p class="quote__text">Maximizing your <span class="keyword">HEALTH</span><br>is about nurturing<br>your body, heart and mind.</p>
      <p class="quote__author">- Mara Vellini</p>
    </div>
    <span class="handle">@thelumencompass</span>
  </section>

  <section class="post post--health">
    <div class="quote">
      <p class="quote__text">When you maximize your <span class="keyword">HEALTH</span>,<br>you gain life and energy to do<br>more of the things you love<br>with the people you love.</p>
      <p class="quote__author">- Mara Vellini</p>
    </div>
    <span class="handle">@thelumencompass</span>
  </section>

  <section class="post post--purpose">
    <div class="quote">
      <p class="quote__text">Companies and people who are<br><span class="keyword">PURPOSE</span>-driven maximize their<br>potential and impact in the world.</p>
      <p class="quote__author">- Mara Vellini</p>
    </div>
    <span class="handle">@thelumencompass</span>
  </section>

  <section class="post post--purpose">
    <div class="quote">
      <p class="quote__text"><span class="keyword">PURPOSE</span>-driven means doing<br>whatever you are doing,<br>consciously thinking on<br>why it is important.</p>
      <p class="quote__author">- Mara Vellini</p>
    </div>
    <span class="handle">@thelumencompass</span>
  </section>

  <section class="post post--purpose">
    <div class="quote">
      <p class="quote__text">When you are <span class="keyword">PURPOSE</span>-driven<br>you live a fulfilling life and<br>you are true to yourself.</p>
      <p class="quote__author">- Mara Vellini</p>
    </div>
    <span class="handle">@thelumencompass</span>
  </section>

</main>
</body>
</html>
```